8.5 x 11 flyer for Hormone Replacement Services for Women

You created a flyer for us that targets men. This flyer will be similar but it is targeted for women.

Here is website with the info. https://www.larkhavenclinic.com/services/hormone-replacement

The flyer you created - https://www.artboxvilla.com/design/48613927

```html
<!DOCTYPE html>
<html lang="en">
<head>
<meta charset="utf-8">
<title>Larkhaven Clinic – Hormone Replacement Flyer</title>
<link rel="stylesheet" href="https://fonts.googleapis.com/css2?family=Jost:wght@400;500;600;700&family=Lato:wght@400;700&display=swap">
<style>
  :root{
    --orange:#f7a23b;
    --ink:#1d1d1d;
    --body:#2b2b2b;
    --slate:#474747;
    --sky:#dff1fb;
    --sky-deep:#cbe9f8;
    --backdrop:#ececec;
    --white:#ffffff;
  }
  *{box-sizing:border-box;margin:0;padding:0}
  html,body{width:1200px;height:800px;overflow:hidden;background:var(--backdrop)}
  body{position:relative;font-family:"Lato",sans-serif;color:var(--body)}
  .page{position:absolute;top:70px;width:510px;height:660px;overflow:hidden;background:var(--white);box-shadow:0 2px 10px rgba(0,0,0,.12)}
  .page--front{left:52px}
  .page--back{left:638px;background:linear-gradient(160deg,#ffffff 0%,var(--sky) 55%,var(--sky-deep) 100%)}
  .page svg.shapes{position:absolute;inset:0;width:510px;height:660px}
  .abs{position:absolute}

  /* front */
  .brand{left:40px;top:30px;display:flex;flex-direction:column;gap:6px}
  .brand__dot{width:30px;height:30px;border-radius:50%;background:var(--orange)}
  .brand__name{font-family:"Jost",sans-serif;font-weight:600;font-size:38px;line-height:1;color:var(--ink)}
  .hero-title{left:44px;top:160px;font-family:"Jost",sans-serif;font-weight:600;font-size:28px;line-height:30px;letter-spacing:.5px;color:var(--ink)}
  .clinic-name{left:61px;top:316px;font-family:"Jost",sans-serif;font-weight:500;font-size:21px;line-height:1.1;color:var(--orange)}
  .clinic-tag{left:61px;top:345px;font-family:"Jost",sans-serif;font-weight:500;font-size:13.5px;line-height:1.1;color:var(--ink)}
  .intro{left:61px;top:374px;width:392px;font-size:9.1px;line-height:11.3px;color:var(--body)}
  .price{left:60px;top:442px;width:128px;height:128px;border-radius:50%;background:radial-gradient(circle at 40% 35%,#6e6e6e,#3f3f3f);color:var(--white);display:flex;flex-direction:column;justify-content:center;padding-left:20px;font-family:"Jost",sans-serif}
  .price__amount{font-size:40px;font-weight:600;line-height:1}
  .price__unit{font-size:16px;font-weight:500;line-height:1.1}
  .slogan{right:59px;top:450px;text-align:right;font-family:"Jost",sans-serif;font-weight:600;font-size:24px;line-height:28px;letter-spacing:.8px;color:var(--ink)}
  .slogan em{font-style:normal;color:var(--orange)}
  .website{right:61px;top:516px;display:flex;align-items:center;gap:5px;font-size:11px;color:var(--ink)}

  /* footer */
  .footer{left:0;top:583px;width:510px;display:flex;color:var(--white)}
  .footer__col{padding-left:41px;width:254px}
  .footer__col + .footer__col{padding-left:12px;border-left:1px solid rgba(255,255,255,.8)}
  .footer__title{font-family:"Jost",sans-serif;font-weight:500;font-size:12px;margin-bottom:5px}
  .footer__line{display:flex;align-items:center;gap:5px;font-size:7.4px;line-height:13.5px;white-space:nowrap}
  .footer__line svg{flex:none}

  /* back */
  .qa-title{left:42px;top:32px;font-family:"Jost",sans-serif;font-weight:600;font-size:17px;line-height:1;letter-spacing:.4px;color:var(--ink)}
  .qa-title em{font-style:normal;color:var(--orange)}
  .qa-col{top:62px;font-size:8.2px;line-height:10px;color:var(--body)}
  .qa-col--left{left:42px;width:202px}
  .qa-col--right{left:269px;width:210px}
  .qa-q{font-family:"Jost",sans-serif;font-weight:500;font-size:12px;line-height:14.5px;color:var(--ink);margin-bottom:7px}
  .qa-q em{font-style:normal;color:var(--orange)}
  .qa-col p{margin-bottom:7px}
  .qa-block{margin-bottom:10px}
  .ticks{list-style:none;margin-bottom:6px}
  .ticks li{display:flex;align-items:center;gap:4px;line-height:13.2px}
  .ticks li::before{content:"";width:5px;height:5px;border-radius:50%;background:var(--orange)}
</style>
</head>
<body>

<section class="page page--front">
  <svg class="shapes" viewBox="0 0 510 660" aria-hidden="true">
    <defs>
      <linearGradient id="heroFill" x1="0" y1="0" x2="1" y2="1">
        <stop offset="0" stop-color="#e8eef0"/>
        <stop offset=".45" stop-color="#c9c2a8"/>
        <stop offset="1" stop-color="#7f9a5c"/>
      </linearGradient>
      <linearGradient id="skyFill" x1="0" y1="0" x2="0" y2="1">
        <stop offset="0" stop-color="#ffffff"/>
        <stop offset="1" stop-color="#d7eefa"/>
      </linearGradient>
    </defs>
    <rect x="0" y="0" width="510" height="330" fill="url(#heroFill)" role="img" aria-label="Photo: smiling woman in a light blue cardigan outdoors with green vineyard hills behind"/>
    <path d="M0 292 Q220 214 510 306 L510 660 L0 660 Z" fill="var(--orange)"/>
    <path d="M0 300 Q220 224 510 316 L510 660 L0 660 Z" fill="var(--white)"/>
    <path d="M0 310 Q220 236 510 330 L510 660 L0 660 Z" fill="url(#skyFill)"/>
    <path d="M0 470 C150 548 300 568 510 540 L510 556 C300 584 150 566 0 488 Z" fill="var(--slate)"/>
    <path d="M0 492 C150 566 300 590 510 560 L510 660 L0 660 Z" fill="var(--white)"/>
    <path d="M0 500 C150 574 300 598 510 566 L510 660 L0 660 Z" fill="var(--orange)"/>
  </svg>

  <div class="abs brand"><span class="brand__dot"></span><span class="brand__name">Larkhaven</span></div>
  <h1 class="abs hero-title">HORMONE<br>REPLACEMENT<br>SPECIALIST</h1>

  <h2 class="abs clinic-name">Larkhaven Clinic</h2>
  <p class="abs clinic-tag">Health and Wellness Center located in Alderpoint, AZ &amp; Cedarbrook, AZ</p>
  <p class="abs intro">Have you noticed a drop in your energy, mental sharpness, or sex drive? You may have low testosterone, which Larkhaven Clinic treats with testosterone replacement therapy. With offices conveniently located in Cedarbrook and Alderpoint, Arizona, the providers test and treat low testosterone. The goal? Restoring the testosterone levels of your youth. Find out more by calling the office nearest you or booking a consultation online.</p>

  <div class="abs price"><span class="price__amount">$150</span><span class="price__unit">per month</span></div>
  <p class="abs slogan">FEEL <em>AMAZING.</em><br>LIVE <em>BETTER.</em></p>
  <p class="abs website">
    <svg width="10" height="10" viewBox="0 0 10 10"><circle cx="5" cy="5" r="4.2" fill="none" stroke="var(--orange)" stroke-width="1"/><path d="M1 5h8M5 1c-2 2.5-2 5.5 0 8M5 1c2 2.5 2 5.5 0 8" fill="none" stroke="var(--orange)" stroke-width=".8"/></svg>
    www.larkhavenclinic.com
  </p>

  <div class="abs footer">
    <div class="footer__col">
      <p class="footer__title">Larkhaven Clinic, Alderpoint, AZ</p>
      <p class="footer__line"><svg width="7" height="7" viewBox="0 0 10 10"><path d="M2 1l2 2-1 1.5c.8 1.4 1.7 2.3 3 3L7.5 6l2 2-1.5 1.5C4.5 9 1 5.5.5 2Z" fill="var(--white)"/></svg>(appointments): 928-555-0142</p>
      <p class="footer__line"><svg width="7" height="7" viewBox="0 0 10 10"><path d="M2 1l2 2-1 1.5c.8 1.4 1.7 2.3 3 3L7.5 6l2 2-1.5 1.5C4.5 9 1 5.5.5 2Z" fill="var(--white)"/></svg>(general inquiries): 928-555-0142</p>
      <p class="footer__line"><svg width="7" height="8" viewBox="0 0 10 12"><path d="M5 0a4 4 0 0 1 4 4c0 3-4 8-4 8S1 7 1 4a4 4 0 0 1 4-4Z" fill="var(--white)"/><circle cx="5" cy="4" r="1.5" fill="var(--orange)"/></svg>1470 West Orchard Avenue, Suite 12, Alderpoint, AZ 86021</p>
    </div>
    <div class="footer__col">
      <p class="footer__title">Larkhaven Clinic, Cedarbrook, AZ</p>
      <p class="footer__line"><svg width="7" height="7" viewBox="0 0 10 10"><path d="M2 1l2 2-1 1.5c.8 1.4 1.7 2.3 3 3L7.5 6l2 2-1.5 1.5C4.5 9 1 5.5.5 2Z" fill="var(--white)"/></svg>(appointments): 520-555-0186</p>
      <p class="footer__line"><svg width="7" height="7" viewBox="0 0 10 10"><path d="M2 1l2 2-1 1.5c.8 1.4 1.7 2.3 3 3L7.5 6l2 2-1.5 1.5C4.5 9 1 5.5.5 2Z" fill="var(--white)"/></svg>(general inquiries): 520-555-0186</p>
      <p class="footer__line"><svg width="7" height="8" viewBox="0 0 10 12"><path d="M5 0a4 4 0 0 1 4 4c0 3-4 8-4 8S1 7 1 4a4 4 0 0 1 4-4Z" fill="var(--white)"/><circle cx="5" cy="4" r="1.5" fill="var(--orange)"/></svg>388 North Saguaro Road, Suite 210, Cedarbrook, AZ 85093</p>
    </div>
  </div>
</section>

<section class="page page--back">
  <svg class="shapes" viewBox="0 0 510 660" aria-hidden="true">
    <path d="M0 488 C160 548 320 565 510 545 L510 560 C320 582 160 566 0 504 Z" fill="var(--slate)"/>
    <path d="M0 506 C160 570 320 590 510 562 L510 660 L0 660 Z" fill="var(--white)"/>
    <path d="M0 514 C160 578 320 598 510 568 L510 660 L0 660 Z" fill="var(--orange)"/>
  </svg>

  <h2 class="abs qa-title">HORMONE REPLACEMENT <em>Q &amp; A</em></h2>

  <div class="abs qa-col qa-col--left">
    <div class="qa-block">
      <h3 class="qa-q">What is <em>hormone replacement<br>for women?</em></h3>
      <p>Although there's no escaping the march of time, modern medicine can now slow the tell-tale signs of aging through bioidentical hormone replacement. The cutting-edge therapy can be a safe, effective solution to combat the effects of aging with natural hormones that mimic the ones in your own body.</p>
      <p>The treatment helps to restore and balance your hormone levels, with precise doses of progesterone, estrogen, DHEA, and more. The goal is to improve your quality of life by returning your hormone levels to normal.</p>
      <p>Your provider at Larkhaven Clinic recommends hormone replacement to relieve perimenopausal and menopausal symptoms. Menopause occurs at age 52 for the average woman. Through this process, your ovaries make less and less estrogen, causing several uncomfortable symptoms.</p>
      <p>Bioidentical hormones help replace the hormones your body has lost. Bioidentical hormones are produced from plants and contain all of the same properties as the estrogen your body makes. Beyond replacing estrogen, these natural hormones supplement progesterone and other hormones your body has lost.</p>
    </div>
    <div class="qa-block">
      <h3 class="qa-q">Are bioidentical hormones<br><em>better than synthetics?</em></h3>
      <p>Hormones used in traditional replacement therapy are usually made of synthetic materials or animal urine. In comparison, bioidentical hormones are created from plant materials, a more natural alternative.</p>
      <p>The providers at Larkhaven Clinic recommend natural estrogen instead of synthetic estrogen because of its benefits.</p>
    </div>
  </div>

  <div class="abs qa-col qa-col--right">
    <div class="qa-block">
      <h3 class="qa-q">What are the <em>benefits of<br>estrogen hormone therapy?</em></h3>
      <p>Hormone therapy to replace the estrogen you've lost helps to protect you from the following ailments and symptoms:</p>
      <ul class="ticks">
        <li>Heart disease</li><li>Stroke</li><li>Osteoporosis</li><li>Alzheimer's disease and memory disorders</li>
        <li>Urinary incontinence</li><li>Hot flashes</li><li>Mood swings</li><li>Fatigue</li>
      </ul>
      <p>The therapy also helps with vaginal atrophy to restore your intimate wellbeing.</p>
      <p>Your provider at Larkhaven Clinic also recommends balancing estrogen with progesterone to achieve all the benefits of hormone replacement.</p>
    </div>
    <div class="qa-block">
      <h3 class="qa-q">Why is progesterone <em>therapy necessary?</em></h3>
      <p>Progesterone, a hormone secreted by your ovaries until menopause, helps to protect against a number of health conditions, including:</p>
      <ul class="ticks">
        <li>Breast and uterine cancer</li><li>Ovarian cysts</li><li>Fibrocystic disease</li><li>Bone loss</li>
      </ul>
      <p>Progesterone also causes common menopausal symptoms, which is why your provider recommends a balanced regime that includes both estrogen and progesterone.</p>
      <p>If you're experiencing changes in your body because of aging, find out if natural bioidentical hormone therapy is right for you. Call Larkhaven Clinic today, or book a consultation online.</p>
    </div>
  </div>

  <div class="abs footer">
    <div class="footer__col">
      <p class="footer__title">Larkhaven Clinic, Alderpoint, AZ</p>
      <p class="footer__line"><svg width="7" height="7" viewBox="0 0 10 10"><path d="M2 1l2 2-1 1.5c.8 1.4 1.7 2.3 3 3L7.5 6l2 2-1.5 1.5C4.5 9 1 5.5.5 2Z" fill="var(--white)"/></svg>(appointments): 928-555-0142</p>
      <p class="footer__line"><svg width="7" height="7" viewBox="0 0 10 10"><path d="M2 1l2 2-1 1.5c.8 1.4 1.7 2.3 3 3L7.5 6l2 2-1.5 1.5C4.5 9 1 5.5.5 2Z" fill="var(--white)"/></svg>(general inquiries): 928-555-0142</p>
      <p class="footer__line"><svg width="7" height="8" viewBox="0 0 10 12"><path d="M5 0a4 4 0 0 1 4 4c0 3-4 8-4 8S1 7 1 4a4 4 0 0 1 4-4Z" fill="var(--white)"/><circle cx="5" cy="4" r="1.5" fill="var(--orange)"/></svg>1470 West Orchard Avenue, Suite 12, Alderpoint, AZ 86021</p>
    </div>
    <div class="footer__col">
      <p class="footer__title">Larkhaven Clinic, Cedarbrook, AZ</p>
      <p class="footer__line"><svg width="7" height="7" viewBox="0 0 10 10"><path d="M2 1l2 2-1 1.5c.8 1.4 1.7 2.3 3 3L7.5 6l2 2-1.5 1.5C4.5 9 1 5.5.5 2Z" fill="var(--white)"/></svg>(appointments): 520-555-0186</p>
      <p class="footer__line"><svg width="7" height="7" viewBox="0 0 10 10"><path d="M2 1l2 2-1 1.5c.8 1.4 1.7 2.3 3 3L7.5 6l2 2-1.5 1.5C4.5 9 1 5.5.5 2Z" fill="var(--white)"/></svg>(general inquiries): 520-555-0186</p>
      <p class="footer__line"><svg width="7" height="8" viewBox="0 0 10 12"><path d="M5 0a4 4 0 0 1 4 4c0 3-4 8-4 8S1 7 1 4a4 4 0 0 1 4-4Z" fill="var(--white)"/><circle cx="5" cy="4" r="1.5" fill="var(--orange)"/></svg>388 North Saguaro Road, Suite 210, Cedarbrook, AZ 85093</p>
    </div>
  </div>
</section>

</body>
</html>
```